Vice chair

I'm running for a position as vice chair this will be posted in the lunch room cafeteria in this package i posted logos, my picture, sample of old flyers to give you a idea i also wrote literature need help in putting it together like it to look like a million bucks goal win this election I summited lots of pdf files and jpeg look though them to help with your design feel free to contact me to further assist you
Updates

Would like this to be completed by Wednesday

Target Market(s)

My constituents

Font styles to use
Serif

Colors

Designer to choose colors to be used in the design.

Requirements
Must have
• Make it look clean neat
Nice to have
• Nice background

```html
<!DOCTYPE html>
<html lang="en">
<head>
<meta charset="utf-8">
<title>Daniel Morales for Vice Chair</title>
<link href="https://fonts.googleapis.com/css2?family=Open+Sans:wght@400;600;700;800&display=swap" rel="stylesheet">
<style>
  :root {
    --navy: #2e3192;
    --red: #ed1c24;
    --white: #ffffff;
    --ink: #111111;
    --slate-green: #1f5c2a;
  }
  * { margin: 0; padding: 0; box-sizing: border-box; }
  html, body { width: 851px; height: 1200px; overflow: hidden; background: var(--white); }
  body { font-family: "Open Sans", Arial, sans-serif; }
  .flyer { position: relative; width: 851px; height: 1200px; overflow: hidden; background: var(--white); }

  .hero { position: absolute; left: 0; top: 0; width: 851px; height: 408px; }
  .hero-flag { position: absolute; inset: 0;
    background: linear-gradient(160deg, #3b4a9a 0%, #5c6bb5 35%, #e9e6ee 55%, #d23a3f 72%, #f3eef0 86%, #c8303a 100%); }
  .hero-portrait { position: absolute; right: 0; top: 110px; width: 205px; height: 298px;
    background: linear-gradient(180deg, #6d4a38 0%, #b07c5e 45%, #2a2a2a 100%); }
  .hero-swoosh { position: absolute; left: 0; top: 0; }
  .experience { position: absolute; left: 10px; top: 312px; font-weight: 700; font-size: 48px;
    line-height: 46px; color: var(--ink); letter-spacing: 0.5px; }

  .name-band { position: absolute; left: 0; top: 408px; width: 851px; height: 344px; background: var(--navy); }
  .candidate-name { position: absolute; right: 4px; top: 414px; font-size: 49px; font-weight: 600;
    color: var(--white); letter-spacing: 1px; }

  .intro { position: absolute; left: 54px; top: 485px; width: 797px; height: 224px; background: var(--white);
    padding: 10px 10px 0 10px; font-size: 14.6px; line-height: 22.8px; color: var(--ink); }
  .intro p + p { margin-top: 26px; }

  .lower-waves { position: absolute; left: 0; top: 700px; }

  .panel { position: absolute; background: var(--red); color: var(--white); }
  .panel-beliefs { left: 0; top: 778px; width: 262px; height: 312px; padding: 14px 8px 0 11px;
    font-size: 17px; line-height: 26.5px; }
  .panel-beliefs p + p { margin-top: 12px; }
  .panel-closing { left: 290px; top: 728px; width: 304px; height: 360px; padding: 12px 16px 0 18px;
    font-size: 19.5px; line-height: 30.2px; }
  .panel-slate { left: 625px; top: 756px; width: 226px; height: 444px; }

  .slate-name { position: absolute; left: 0; width: 226px; top: 22px; text-align: center;
    font-weight: 800; font-size: 30px; line-height: 30px; color: var(--slate-green); }
  .slate-call { position: absolute; left: 0; width: 226px; top: 90px; text-align: center;
    font-weight: 700; font-size: 27px; line-height: 34px; letter-spacing: -0.5px;
    white-space: nowrap; color: var(--navy); }
  .slate-box { position: absolute; left: 85px; top: 134px; width: 56px; height: 56px;
    border: 1px solid var(--white); }

  .bottom-waves { position: absolute; left: 0; top: 990px; }

  .depots { position: absolute; left: 0; top: 1100px; width: 560px; height: 100px; }
  .depot { position: absolute; width: 96px; height: 96px; border-radius: 50%; }
  .depot-one { left: 38px; top: 0; background: #f47a20; border: 4px solid #c8321e; }
  .depot-two { left: 176px; top: -4px; background: #2f5fae; border: 4px solid #ffffff; }
  .depot-three { left: 318px; top: -6px; background: #ffd91a; border: 4px solid #e3262b; }

  .vote-independent { position: absolute; left: 628px; top: 1118px; color: var(--white);
    font-size: 30px; line-height: 30px; font-weight: 400; letter-spacing: 0.5px; }
  .ballot-box { position: absolute; left: 726px; top: 1061px; width: 101px; height: 85px;
    border: 2px solid var(--white); }
</style>
</head>
<body>
<main class="flyer">

  <section class="hero">
    <div class="hero-flag" role="img" aria-label="Waving American flag photograph"></div>
    <svg class="hero-swoosh" width="851" height="408" viewBox="0 0 851 408" aria-hidden="true">
      <path d="M0 0 H420 C300 20 140 40 0 60 Z" fill="var(--navy)"/>
      <path d="M0 70 C150 70 260 100 300 122 C200 120 90 118 0 112 Z" fill="var(--red)"/>
      <path d="M600 0 H851 V120 C790 60 700 20 600 0 Z" fill="var(--red)"/>
      <path d="M620 0 H720 C780 20 830 40 851 60 V90 C800 50 720 15 620 0 Z" fill="var(--navy)"/>
    </svg>
    <div class="hero-portrait" role="img" aria-label="Portrait photograph of the candidate"></div>
    <h2 class="experience">20 Years<br>Experience</h2>
  </section>

  <section class="name-band"></section>
  <h1 class="candidate-name">DANIEL MORALES</h1>

  <article class="intro">
    <p>I, Daniel Morales for those who don’t know me would like to introduce myself. I have always been approachable and helpful whether you are a probationary officer or veteran operator with knowledge or information. We must protect our union rules for ourselves and most important our children.</p>
    <p>I would like this opportunity to run as your Vice Chair. A person you can trust and believe in me. Positive and motivations are my main keys for progress and for change in my campaign. When there are no leaders to look up to one therefore must become one. I do believe I’m the right person for this position. So please come out and support me and vote me as your Vice Chair.</p>
  </article>

  <svg class="lower-waves" width="851" height="120" viewBox="0 0 851 120" aria-hidden="true">
    <path d="M0 52 V120 H851 V52 Z" fill="var(--navy)"/>
    <path d="M0 62 C200 100 500 110 851 78 V120 H0 Z" fill="var(--white)"/>
    <path d="M0 84 C260 112 560 116 851 92 V120 H0 Z" fill="var(--white)"/>
  </svg>

  <section class="panel panel-beliefs">
    <p>Past Union member of Transit Local 412 believes in. There is a collective bargaining agreement in place and no management is above the law to violate it.</p>
    <p>Past Union member of Transit Local 738 believes in. There is a house that divided cannot stand alone.</p>
  </section>

  <section class="panel panel-closing">
    <p>In Closing, I believe that our union does not stand out individually achievement we must stand out for collective advancement for all. We must always continue to stand &amp; fight together so we can win together because success is never owned, it is rented and the rent is due every day.</p>
  </section>

  <section class="panel panel-slate">
    <div class="slate-name">FORWARD<br>TOGETHER</div>
    <div class="slate-call">Vote the slate</div>
    <svg class="slate-box" viewBox="0 0 56 56" aria-hidden="true">
      <path d="M8 6 L48 50 M48 6 L8 50" stroke="var(--navy)" stroke-width="9"/>
    </svg>
  </section>

  <svg class="bottom-waves" width="851" height="210" viewBox="0 0 851 210" aria-hidden="true">
    <path d="M0 100 C300 110 600 60 851 -20 V30 C600 120 300 150 0 150 Z" fill="var(--navy)"/>
    <path d="M0 150 C300 150 600 120 851 30 V210 H0 Z" fill="var(--red)"/>
    <path d="M0 150 C300 150 600 122 851 40 V52 C600 134 300 164 0 164 Z" fill="var(--white)"/>
  </svg>

  <div class="depots">
    <div class="depot depot-one" role="img" aria-label="Depot badge"></div>
    <div class="depot depot-two" role="img" aria-label="Depot badge"></div>
    <div class="depot depot-three" role="img" aria-label="Depot badge"></div>
  </div>

  <svg class="ballot-box" viewBox="0 0 101 85" aria-hidden="true">
    <path d="M28 16 L72 70 M72 16 L28 70" stroke="var(--ink)" stroke-width="11"/>
  </svg>
  <p class="vote-independent">VOTE<br>INDEPENDENT</p>

</main>
</body>
</html>
```